We are an education and business training and consulting company focused on helping companies maximize their growth potential. Our goal is provide targeted human resource solutions to organizational problems.
Target Market(s)
School districts and businesses of all types
Industry/Entity Type
Education
Contact Information for Business Card
Crestline and Harbor Partners LLC
Walter Pruitt president
Business and Education Training and Consulting
517 Birch Hollow Lane
Naples, Florida 34987
(239) 555-0147
Walter.pruitt@crestlineharborpartners.example
Font styles to use
Colors
Designer to choose colors to be used in the design.
Look and feel

```html
<!DOCTYPE html>
<html lang="en">
<head>
<meta charset="utf-8">
<title>Crestline and Harbor Partners LLC – Business Card</title>
<link rel="stylesheet" href="https://fonts.googleapis.com/css2?family=Exo+2:wght@300&family=Roboto+Condensed:wght@700&family=Roboto:wght@400&display=swap">
<style>
  :root {
    --stage: #c6c6c6;
    --navy: #1b3454;
    --white: #ffffff;
    --band: #d9d9d9;
    --ink: #1e1e1e;
    --muted: #b5bdc9;
    --rule: #7f8ea3;
  }
  * { margin: 0; padding: 0; box-sizing: border-box; }
  html, body {
    width: 1200px;
    height: 913px;
    overflow: hidden;
    background: var(--stage);
    font-family: "Roboto", Arial, sans-serif;
  }
  .card {
    position: absolute;
    width: 714px;
    height: 414px;
    border-radius: 18px;
    overflow: hidden;
  }

  /* Front side */
  .card--front {
    left: 58px;
    top: 35px;
    background: var(--navy);
  }
  .brand {
    position: absolute;
    display: flex;
    align-items: center;
    gap: 18px;
  }
  .brand__square {
    flex: none;
    border-style: solid;
  }
  .brand__name {
    font-family: "Exo 2", "Trebuchet MS", sans-serif;
    font-weight: 300;
    line-height: 1.15;
  }
  .card--front .brand {
    left: 134px;
    top: 140px;
  }
  .card--front .brand__square {
    width: 60px;
    height: 60px;
    border-width: 4px;
    border-color: var(--white);
  }
  .card--front .brand__name {
    color: var(--white);
    font-size: 36px;
  }
  .tagline {
    position: absolute;
    left: 135px;
    top: 297px;
    width: 452px;
    padding: 9px 0 10px;
    border-top: 1px solid var(--rule);
    border-bottom: 1px solid var(--rule);
    color: var(--muted);
    font-size: 20px;
    letter-spacing: 0.1px;
  }

  /* Back side */
  .card--back {
    left: 439px;
    top: 472px;
    background: var(--white);
  }
  .card--back .brand {
    right: 34px;
    top: 40px;
    gap: 12px;
  }
  .card--back .brand__square {
    width: 40px;
    height: 40px;
    border-width: 3px;
    border-color: var(--navy);
  }
  .card--back .brand__name {
    color: var(--navy);
    font-size: 23px;
  }
  .person {
    position: absolute;
    left: 46px;
    top: 144px;
  }
  .person__name {
    font-family: "Roboto Condensed", "Arial Narrow", sans-serif;
    font-weight: 700;
    font-size: 32px;
    color: var(--ink);
  }
  .person__title {
    margin-top: 8px;
    font-size: 21px;
    color: var(--navy);
  }
  .contact {
    position: absolute;
    left: 0;
    top: 241px;
    width: 100%;
    height: 173px;
    background: var(--band);
    list-style: none;
    padding: 24px 0 0 44px;
  }
  .contact__item {
    display: flex;
    align-items: center;
    height: 40px;
    font-size: 22px;
    color: var(--ink);
  }
  .contact__icon {
    width: 26px;
    height: 26px;
    margin-right: 16px;
    fill: var(--navy);
    flex: none;
  }
</style>
</head>
<body>

<section class="card card--front" aria-label="Card front">
  <div class="brand">
    <span class="brand__square"></span>
    <span class="brand__name">Crestline and Harbor<br>Partners LLC</span>
  </div>
  <p class="tagline">Business and Education Training and Consulting</p>
</section>

<section class="card card--back" aria-label="Card back">
  <div class="brand">
    <span class="brand__square"></span>
    <span class="brand__name">Crestline and Harbor<br>Partners LLC</span>
  </div>

  <div class="person">
    <h1 class="person__name">Walter Pruitt</h1>
    <p class="person__title">President</p>
  </div>

  <ul class="contact">
    <li class="contact__item">
      <svg class="contact__icon" viewBox="0 0 24 24" aria-hidden="true">
        <path d="M6.6 10.8c1.4 2.8 3.8 5.1 6.6 6.6l2.2-2.2c.3-.3.7-.4 1-.2 1.1.4 2.3.6 3.6.6.6 0 1 .4 1 1V20c0 .6-.4 1-1 1C10.6 21 3 13.4 3 4c0-.6.4-1 1-1h3.5c.6 0 1 .4 1 1 0 1.3.2 2.5.6 3.6.1.3 0 .7-.2 1z"/>
      </svg>
      <span>(239) 555-0147</span>
    </li>
    <li class="contact__item">
      <svg class="contact__icon" viewBox="0 0 24 24" aria-hidden="true">
        <rect x="11" y="2" width="2.4" height="20"/>
        <path d="M13 5h7l3 3-3 3h-7z"/>
        <path d="M11 10H4l-3 3 3 3h7z"/>
      </svg>
      <span>517 Birch Hollow Lane Naples, Florida 34987</span>
    </li>
    <li class="contact__item">
      <svg class="contact__icon" viewBox="0 0 24 24" aria-hidden="true">
        <path d="M2 5h20v2.2l-10 6-10-6z"/>
        <path d="M2 9.5l10 6 10-6V19H2z"/>
      </svg>
      <span>Walter.pruitt@crestlineharborpartners.example</span>
    </li>
  </ul>
</section>

</body>
</html>
```